Hello everyone,
I need someone to design a Business Card for my new company. It's called Norvakeep and we give procurement services of Chilean Salmon and Seafood in General. More specifically we are purchasing agents, quality inspectors and we help with general papework and logistics. Maybe in the future can open to some agriculture items such as Meat, Dairy Products and Fruits.
All this focused in international clients that cannot have the support they need when buying items from Chile.
A main concept is reliability.

Thank you in advance.

Esteban.

Target Market(s)

Salmon and Seafood Importers from all world.

Industry/Entity Type

Business

Contact Information for Business Card

The Name: Esteban Ruiz Pardo
My Mobile: +56 9 47316258
My Location: Bahía Serena, Chile

Font styles to use
Serif
Sans Serif

Requirements
Must have
• The company name and a logo.
Nice to have
• Some full color on the back side.
Should not have
• No modern shapes. Just a rectangular business card. Remember that has to be accepted by a lot of different cultures, even senior Japanese clients.

```html
<!DOCTYPE html>
<html lang="en">
<head>
<meta charset="utf-8">
<title>Norvakeep Business Card</title>
<link href="https://fonts.googleapis.com/css2?family=Oswald:wght@400;500;700&family=Arimo:wght@400;700&display=swap" rel="stylesheet">
<style>
  :root {
    --bg: #ecebe8;
    --forest: #234522;
    --forest-deep: #1b3619;
    --leaf: #8cc043;
    --leaf-pale: #eef4e4;
    --ink: #111111;
    --grey: #8a8a8a;
    --white: #ffffff;
  }
  html, body {
    margin: 0;
    width: 1200px;
    height: 1000px;
    overflow: hidden;
    background: var(--bg);
  }
  .canvas { position: relative; width: 1200px; height: 1000px; }
  .card { position: absolute; box-shadow: 0 6px 18px rgba(0,0,0,.25); overflow: hidden; }

  /* Back side */
  .card-back {
    left: 70px; top: 40px; width: 800px; height: 440px;
    background: var(--forest);
  }
  .card-back .top-band {
    position: absolute; left: 0; top: 0; width: 100%; height: 220px;
    background: var(--forest-deep);
  }
  .card-back .leaf-band {
    position: absolute; left: 0; top: 300px; width: 100%; height: 90px;
    background: var(--leaf);
  }
  .card-back .wordmark {
    position: absolute; left: 70px; top: 110px;
    font-family: 'Oswald', sans-serif; font-weight: 500;
    font-size: 72px; letter-spacing: 20px; color: var(--leaf);
    margin: 0; line-height: 1;
  }
  .card-back .mark-name {
    position: absolute; left: 0; width: 100%; top: 300px; height: 90px;
    display: flex; align-items: center; justify-content: center;
    font-family: 'Oswald', sans-serif; font-weight: 700;
    font-size: 60px; color: var(--white); line-height: 1;
  }

  /* Front side */
  .card-front {
    left: 345px; top: 485px; width: 725px; height: 425px;
    background: var(--white);
  }
  .card-front .faint-name {
    position: absolute; right: 20px; top: 40px;
    font-family: 'Oswald', sans-serif; font-weight: 700;
    font-size: 80px; color: var(--leaf-pale); line-height: 1;
  }
  .card-front .brand {
    position: absolute; left: 80px; top: 95px;
  }
  .brand .brand-name {
    font-family: 'Oswald', sans-serif; font-weight: 700;
    font-size: 64px; color: var(--leaf); line-height: 1; margin: 0;
  }
  .brand .brand-sub {
    font-family: 'Oswald', sans-serif; font-weight: 500;
    font-size: 22px; letter-spacing: 5px; color: var(--grey);
    margin: 46px 0 0; line-height: 1;
  }
  .contact {
    position: absolute; left: 350px; top: 278px;
    font-family: 'Arimo', sans-serif;
  }
  .contact .person {
    font-weight: 700; font-size: 20px; color: var(--ink); margin: 0 0 22px;
  }
  .contact .line {
    display: flex; align-items: center; gap: 14px;
    font-size: 19px; color: var(--leaf); margin: 0 0 8px;
  }
  .contact svg { width: 20px; height: 20px; fill: var(--ink); flex: none; }
</style>
</head>
<body>
<div class="canvas">
  <section class="card card-back">
    <div class="top-band"></div>
    <div class="leaf-band"></div>
    <h1 class="wordmark">NORVAKEEP</h1>
    <div class="mark-name">Norvakeep</div>
  </section>

  <section class="card card-front">
    <div class="faint-name" aria-hidden="true">Norvakeep</div>
    <div class="brand">
      <p class="brand-name">Norvakeep</p>
      <p class="brand-sub">NORVAKEEP</p>
    </div>
    <div class="contact">
      <p class="person">ESTEBAN RUIZ PARDO</p>
      <p class="line">
        <svg viewBox="0 0 24 24" aria-hidden="true"><path d="M3 8c0-2 4-4 9-4s9 2 9 4v2h-5V8.5c-1-.4-2.4-.6-4-.6s-3 .2-4 .6V10H3z M6 12h12l2 8H4z M10 15a2 2 0 1 0 4 0a2 2 0 1 0-4 0z"/></svg>
        <span>+56 9 47316258</span>
      </p>
      <p class="line">
        <svg viewBox="0 0 24 24" aria-hidden="true"><path d="M12 2a7 7 0 0 0-7 7c0 5 7 13 7 13s7-8 7-13a7 7 0 0 0-7-7zm0 10a3 3 0 1 1 0-6a3 3 0 0 1 0 6z"/></svg>
        <span>Bahía Serena, Chile</span>
      </p>
    </div>
  </section>
</div>
</body>
</html>
```